Modern and Clean Web Re-Design Project

We have 2 companies in similar industries: Printing and Mail Preparation/Fulfillment. We prefer sites that are clean and easy to navigate.Our printing company, Harbourline Press Works' website, hpwgroup-example.ca is outdated needs revamping. We have rebranded our logo and are looking for a new design that is clean, modern and geared to other corporations and business in the downtown Toronto area. Our mailing company, The Parcel Loft (theparcelloft-example.ca) needs a website as well. This company is in the Direct Mail and letter shop business, which essentially is addressing/personalizing people's printed matter and preparing it for either the Canadian or US postal service. The Parcel Loft specializes in not-for-profit and corporate sectors.Please see our logos to get an idea of the colors and look we want. For all intensive purposes, the sites can look similar in design all we want is that each site has the appropriate corporate colors and is a bit different so they don't look identical as the two business run as separate corporations.The content of the website should be easily changed by our staff and we want it to be setup to optimized for SEO based on the keywords we want. We are looking for someone to work on this project immediately

After doing some thinking, I would like the site to be more modern but the non flash sites that I have seen so far Im finding life-less and while I want something clean, not overly busy and corporate looking, I dont want the design to be bland looking.

Please design with the previous specs in mind but with a twist as mentioned above.

Thanks
Dorian

Target Market(s)

See above

Industry/Entity Type

Printing

Requirements
Must have
• Must match the design and style of each respective logoSee the attached impage of the front of our offices to have an idea of our lookWe must be able to edit the content ourselves without any fancy programs or tools.Must be SEO optimized
Nice to have
• An online order form that can be emailed to us for quotes.....perhaps a page with a bunch of fields that have drop down menus....
Should not have
• Should not be overly busy. I want it to be clean and simple but informative without being hard to navigate

```html
<!DOCTYPE html>
<html lang="en">
<head>
<meta charset="utf-8">
<title>Harbourline Press Works</title>
<link rel="stylesheet" href="https://fonts.googleapis.com/css2?family=Lato:ital,wght@0,400;0,700;0,900;1,400;1,700&family=Arimo:wght@400;700&display=swap">
<style>
:root{
  --orange:#f0a020;
  --orange-dark:#e08a10;
  --red:#e9473a;
  --quote-top:#f9855a;
  --quote-bottom:#ee5a2a;
  --brown:#a98462;
  --footer:#8f6b4f;
  --footer-dark:#6b4e37;
  --ink:#222;
  --body:#444;
  --muted:#666;
  --line:#ddd;
  --panel:#f6f6f6;
  --white:#fff;
}
*{box-sizing:border-box;margin:0;padding:0}
html,body{width:1200px;height:1189px;overflow:hidden;background:var(--white)}
body{font-family:"Arimo",Arial,sans-serif;color:var(--body)}
.canvas{position:relative;width:1200px;height:1189px;overflow:hidden;
  background:linear-gradient(#e9e9e9 0,#f7f7f7 180px,#ececec 276px,var(--white) 276px)}
.abs{position:absolute}

/* header */
.brand{left:247px;top:30px;width:220px}
.brand-mark{display:flex;align-items:center;gap:10px;font-family:"Lato",sans-serif;font-weight:900;font-size:40px;color:var(--orange-dark);letter-spacing:1px}
.brand-mark .dot{width:14px;height:14px;border-radius:50%;background:var(--red)}
.brand-name{margin-top:2px;font-family:"Lato",sans-serif;font-weight:900;font-size:12px;color:var(--orange-dark);letter-spacing:1.2px;text-transform:uppercase}
.call-box{left:740px;top:12px;width:235px;height:53px;background:var(--brown);border-radius:4px;color:var(--white);padding:7px 0 0 16px;box-shadow:0 1px 2px rgba(0,0,0,.2)}
.call-row{display:flex;align-items:center;gap:10px}
.call-row.phone{font-family:"Lato",sans-serif;font-weight:900;font-size:17px}
.call-row.mail{font-size:11px;margin-top:4px}

/* navigation */
.nav{left:224px;top:121px;width:750px;height:41px;background:var(--orange);display:flex;align-items:center}
.nav-home{width:36px;height:41px;background:var(--red);display:flex;align-items:center;justify-content:center}
.nav a{color:var(--white);font-family:"Lato",sans-serif;font-weight:700;font-size:11px;text-decoration:none;text-transform:uppercase;margin-left:14px}
.nav-pickup{position:absolute;right:0;top:0;height:41px;width:170px;background:var(--brown);border-radius:22px 0 0 0;display:flex;align-items:center;gap:8px;padding-left:20px;color:var(--white);font-family:"Lato",sans-serif;font-weight:700;font-size:10.5px}

/* hero */
.hero{left:224px;top:162px;width:509px;height:234px;background:linear-gradient(90deg,#f3eeea 0,#f1ebe6 40%,#e9dfd6 100%);border:1px solid #e2dcd6}
.hero-photo{position:absolute;right:0;top:0;width:250px;height:232px;background:linear-gradient(135deg,#e9e2da 0,#d9533f 35%,#e7d6c4 55%,#c94a3a 75%,#ebe3db 100%);opacity:.85}
.hero h1{position:absolute;left:20px;top:55px;font-family:"Lato",sans-serif;font-weight:400;font-size:23px;line-height:29px;color:var(--ink)}
.hero p{position:absolute;left:21px;top:117px;width:230px;font-size:10px;line-height:12px;color:#555}
.btn{position:absolute;height:24px;border-radius:3px;font-family:"Lato",sans-serif;font-size:10px;display:flex;align-items:center;justify-content:center}
.btn-grey{left:22px;top:162px;width:84px;background:linear-gradient(#f2f2f2,#cfcfcf);border:1px solid #b9b9b9;color:#333}
.btn-orange{left:115px;top:162px;width:84px;background:linear-gradient(var(--quote-top),var(--quote-bottom));color:var(--white);border:1px solid #d9501f}

/* quote form */
.quote{left:733px;top:168px;width:241px;height:379px;background:#fdf8ef;border:1px solid #f1c98a;border-top:none}
.quote-head{height:36px;background:linear-gradient(var(--quote-top),var(--quote-bottom));color:var(--white);font-family:"Lato",sans-serif;font-size:16px;display:flex;align-items:center;justify-content:center;border-radius:3px 3px 0 0}
.quote-fields{padding:12px 9px 0}
.field{height:29px;margin-bottom:3px;background:var(--white);border:1px solid #d7d0c4;border-radius:2px;font-family:"Lato",sans-serif;font-size:10.5px;color:#333;padding-left:6px;display:flex;align-items:center;position:relative}
.field .req{color:var(--red);margin-left:2px;position:relative;top:-3px}
.field svg{position:absolute;right:7px}
.quote-submit{margin:6px 9px 0;height:38px;background:linear-gradient(var(--quote-top),var(--quote-bottom));border-radius:3px;color:var(--white);font-family:"Lato",sans-serif;font-size:17px;display:flex;align-items:center;justify-content:center;text-transform:uppercase}
.quote-note{text-align:center;font-family:"Lato",sans-serif;font-style:italic;font-weight:700;font-size:8.5px;color:#555;margin-top:13px}

/* welcome */
.welcome{left:224px;top:407px;width:497px;height:140px;background:var(--panel);border:1px solid var(--line);border-radius:3px}
.welcome h2{position:absolute;left:17px;top:14px;font-weight:400;font-size:13.5px;color:var(--ink)}
.welcome .flag{position:absolute;left:0;top:9px;width:4px;height:26px;background:var(--orange)}
.welcome p{position:absolute;left:17px;top:44px;width:464px;font-size:10.2px;line-height:15.5px;color:#444}
.read-more{position:absolute;font-size:8.5px;font-weight:700;color:#f07845}

/* feature cards */
.card{top:559px;width:241px;height:235px;background:var(--white);border:1px solid var(--line);border-radius:3px;box-shadow:0 1px 2px rgba(0,0,0,.06)}
.card-head{height:32px;background:linear-gradient(#f7f7f7,#e2e2e2);display:flex;align-items:center;justify-content:center;font-size:13px;color:var(--ink);border-bottom:1px solid #d8d8d8}
.card-photo{position:absolute;left:17px;top:42px;width:206px;height:88px;border-radius:3px}
.card ul{position:absolute;left:17px;top:139px;width:210px;list-style:none}
.card li{position:relative;padding-left:16px;font-size:10px;line-height:12px;color:#444;margin-bottom:12px}
.card li::before{content:"";position:absolute;left:0;top:2px;width:6px;height:6px;border:1px solid #999;border-radius:50%}
.testimonial{position:absolute;left:17px;top:139px;width:206px;font-size:10px;line-height:12.5px;color:#333;text-align:justify;padding-left:18px}
.testimonial .q{position:absolute;left:0;top:-2px;font-family:"Lato",sans-serif;font-weight:900;font-size:24px;line-height:22px;color:#333}
.testimonial .who{display:block;margin-top:10px;font-weight:700;font-size:9.5px;color:#111}

/* clients */
.divider{left:240px;top:812px;width:720px;height:18px;background:radial-gradient(ellipse at 50% 0,rgba(0,0,0,.22),rgba(0,0,0,0) 70%)}
.clients-title{left:0;top:840px;width:1200px;text-align:center;font-size:13px;color:var(--ink);letter-spacing:.5px}
.clients{left:320px;top:885px;width:560px;display:flex;justify-content:space-between;align-items:center}
.client{display:flex;align-items:center;gap:6px;font-family:"Arimo",sans-serif;font-weight:700;font-size:14px;color:#111}
.client i{display:block;width:10px;height:10px;background:#111;border-radius:50%}

/* footer */
.footer{left:0;top:954px;width:1200px;height:214px;background:var(--footer);color:var(--white)}
.footer h3{position:absolute;top:30px;font-weight:400;font-size:13px}
.footer .col{position:absolute;top:64px;font-size:10px;line-height:15px}
.contact-col{width:225px}
.contact-row{display:flex;gap:8px;margin-bottom:9px}
.contact-row svg{flex:none;margin-top:2px}
.links a{display:block;color:var(--white);text-decoration:none}
.social{display:grid;grid-template-columns:repeat(2,auto);gap:4px;width:130px}
.social span{display:flex;align-items:center;justify-content:center;height:18px;padding:0 4px;border-radius:3px;font-size:8px;font-weight:700;color:var(--white)}
.like{margin-top:8px;display:inline-flex;align-items:center;gap:5px;background:#f4f4f4;border:1px solid #ccc;border-radius:3px;height:22px;padding:0 6px;color:#333;font-size:8.5px}
.like b{background:#fff;border:1px solid #bbb;padding:0 4px;font-weight:400}
.feedback-col{width:186px}
.fb-field{width:185px;height:24px;margin-bottom:5px;background:linear-gradient(#d9d9d9,#efefef);border:1px solid #bfbfbf;border-radius:2px;color:#333;font-size:9.5px;line-height:12px;padding:5px 8px}
.fb-field.msg{height:48px}
.fb-submit{position:absolute;left:100px;top:111px;width:86px;height:30px;background:linear-gradient(var(--quote-top),var(--quote-bottom));border-radius:3px;display:flex;align-items:center;justify-content:center;font-weight:700;font-size:11px}
.copyright{left:0;top:1168px;width:1200px;height:21px;background:var(--footer-dark);color:var(--white);font-size:10px;display:flex;align-items:center;justify-content:center}
</style>
</head>
<body>
<div class="canvas">

  <header>
    <div class="abs brand">
      <div class="brand-mark"><span class="dot"></span>HPW</div>
      <div class="brand-name">Harbourline Press Works</div>
    </div>
    <div class="abs call-box">
      <div class="call-row phone">
        <svg width="16" height="16" viewBox="0 0 24 24"><path fill="#fff" d="M6.6 10.8a15 15 0 0 0 6.6 6.6l2.2-2.2c.3-.3.7-.4 1-.2 1.1.4 2.3.6 3.6.6.6 0 1 .4 1 1V20c0 .6-.4 1-1 1A17 17 0 0 1 3 4c0-.6.4-1 1-1h3.5c.6 0 1 .4 1 1 0 1.3.2 2.5.6 3.6.1.3 0 .7-.2 1z"/></svg>
        Call Us:&nbsp; (416) 555-0142
      </div>
      <div class="call-row mail">
        <svg width="14" height="10" viewBox="0 0 14 10"><rect width="14" height="10" rx="1" fill="#fff"/><path d="M0 1l7 5 7-5" stroke="#a98462" stroke-width="1.3" fill="none"/></svg>
        mac@hpwgroup-example.ca
      </div>
    </div>
  </header>

  <nav class="abs nav">
    <span class="nav-home"><svg width="14" height="13" viewBox="0 0 14 13"><path fill="#fff" d="M7 0l7 6h-2v7H9V9H5v4H2V6H0z"/></svg></span>
    <a href="#">Who we are</a>
    <a href="#">What we do</a>
    <a href="#">Email us your file</a>
    <a href="#">Contact us</a>
    <span class="nav-pickup">
      <svg width="28" height="28" viewBox="0 0 28 28"><rect x="3" y="6" width="22" height="18" fill="#f4eee6"/><rect x="3" y="6" width="22" height="5" fill="#dccfbf"/><rect x="11" y="6" width="6" height="8" fill="#c9b49c"/></svg>
      Free pickup &amp; Delivery
    </span>
  </nav>

  <section class="abs hero">
    <div class="hero-photo" role="img" aria-label="Photo of rolled printed paper in red and cream tones"></div>
    <h1>High-quality product<br>under strict deadlines</h1>
    <p>Etultrices posuere cubilia Curae; Suspendisse a tellus quis libero euismod egestas nam.dolor mauris.</p>
    <span class="btn btn-grey">Learn more</span>
    <span class="btn btn-orange">Get Quote</span>
  </section>

  <aside class="abs quote">
    <div class="quote-head">Get Quote</div>
    <div class="quote-fields">
      <div class="field">Enter name<span class="req">*</span></div>
      <div class="field">Company</div>
      <div class="field">Country</div>
      <div class="field">Address<span class="req">*</span></div>
      <div class="field">Email<span class="req">*</span></div>
      <div class="field">Mobile number<span class="req">*</span></div>
      <div class="field">Type of service I want<span class="req">*</span>
        <svg width="10" height="7" viewBox="0 0 10 7"><path d="M1 1l4 4 4-4" stroke="#222" stroke-width="2" fill="none"/></svg></div>
      <div class="field">Upload a file
        <svg width="11" height="11" viewBox="0 0 11 11"><circle cx="4.5" cy="4.5" r="3.3" stroke="#9a7657" stroke-width="1.8" fill="none"/><path d="M7 7l3.3 3.3" stroke="#9a7657" stroke-width="2"/></svg></div>
    </div>
    <div class="quote-submit">Submit my quote</div>
    <div class="quote-note">Field marked with * are mandatory</div>
  </aside>

  <section class="abs welcome">
    <span class="flag"></span>
    <h2>Welcome To HPW</h2>
    <p>We maintain absolute integrity in every aspect of our operation. By using our experience to understand our customers’ expectations, we show an uncommon commitment to achieving a high-quality product under strict deadlines. It is the customers who set the standards we strive to achieve. We are professionals who bring unique and specialized skills you can depend on.</p>
    <span class="read-more" style="right:16px;top:120px">Read more</span>
  </section>

  <article class="abs card" style="left:224px">
    <div class="card-head">Our Process</div>
    <div class="card-photo" role="img" aria-label="Photo of a person holding a colour swatch fan" style="background:linear-gradient(90deg,#e85c8a 0,#f4c24a 25%,#8fc6e0 45%,#d8b59c 60%,#6b4a3a 100%)"></div>
    <ul>
      <li>Vestibulum ante ipsum primis in faucibus orci luctus.</li>
      <li>etultrices posuere cubilia Curae; Suspendisse a tellus quis libero euismod egestas nam.dolor mauris.</li>
    </ul>
    <span class="read-more" style="right:18px;top:216px">Read more</span>
  </article>

  <article class="abs card" style="left:478px">
    <div class="card-head">Grow Your Business</div>
    <div class="card-photo" role="img" aria-label="Photo of a hand stacking coins" style="background:linear-gradient(#d9634a 0,#e8a88a 45%,#c9b7a4 70%,#8a7a68 100%)"></div>
    <ul>
      <li>Vestibulum ante ipsum primis in faucibus orci luctus.</li>
      <li>etultrices posuere cubilia Curae; Suspendisse a tellus quis libero euismod egestas nam.dolor mauris.</li>
    </ul>
    <span class="read-more" style="right:18px;top:216px">Read more</span>
  </article>

  <article class="abs card" style="left:733px">
    <div class="card-head">Testimonials</div>
    <div class="card-photo" role="img" aria-label="Photo of a cheerful businessman with raised arms" style="background:linear-gradient(135deg,#9cc3e6 0,#d8e6f2 45%,#b9cde0 70%,#7fa6cc 100%)"></div>
    <p class="testimonial"><span class="q">“</span>We are so much impressed by the HPW services They were so fantastic at job. Their print services are just amazing...<span class="who">Alina Morrow, Business person</span></p>
    <span class="read-more" style="right:18px;top:216px">More testimonials</span>
  </article>

  <div class="abs divider"></div>
  <div class="abs clients-title">CLIENTS</div>
  <div class="abs clients">
    <span class="client"><i></i>Loopcast</span>
    <span class="client">Playfield</span>
    <span class="client">Discora</span>
    <span class="client">Fundry</span>
    <span class="client">Berrynet</span>
    <span class="client">Northpeak</span>
  </div>

  <footer class="abs footer">
    <h3 style="left:224px">Contact Us</h3>
    <div class="col contact-col" style="left:224px">
      <div class="contact-row">
        <svg width="11" height="14" viewBox="0 0 11 14"><path fill="#f0a020" d="M5.5 0A5.5 5.5 0 0 0 0 5.5C0 9.6 5.5 14 5.5 14S11 9.6 11 5.5A5.5 5.5 0 0 0 5.5 0z"/><circle cx="5.5" cy="5.5" r="2" fill="#8f6b4f"/></svg>
        <span>85 Harbourfront Lane<br>Toronto, Ontario<br>M0X 4Z9</span>
      </div>
      <div class="contact-row" style="margin-bottom:3px">
        <svg width="12" height="12" viewBox="0 0 24 24"><path fill="#f0a020" d="M6.6 10.8a15 15 0 0 0 6.6 6.6l2.2-2.2c.3-.3.7-.4 1-.2 1.1.4 2.3.6 3.6.6.6 0 1 .4 1 1V20c0 .6-.4 1-1 1A17 17 0 0 1 3 4c0-.6.4-1 1-1h3.5c.6 0 1 .4 1 1 0 1.3.2 2.5.6 3.6.1.3 0 .7-.2 1z"/></svg>
        <span>416-555-0187</span>
      </div>
      <div class="contact-row" style="margin-bottom:3px">
        <svg width="12" height="12" viewBox="0 0 12 12"><rect x="3" y="0" width="6" height="4" fill="#f0a020"/><rect x="0" y="4" width="12" height="5" rx="1" fill="#f0a020"/><rect x="3" y="8" width="6" height="4" fill="#f7c76a"/></svg>
        <span>416-555-0187</span>
      </div>
      <div class="contact-row">
        <svg width="12" height="9" viewBox="0 0 14 10"><rect width="14" height="10" rx="1" fill="#f0a020"/><path d="M0 1l7 5 7-5" stroke="#8f6b4f" stroke-width="1.3" fill="none"/></svg>
        <span>dorian@hpwgroup-example.ca /<br>mac@hpwgroup-example.ca</span>
      </div>
    </div>

    <h3 style="left:464px">Links</h3>
    <div class="col links" style="left:464px">
      <a href="#">Home</a><a href="#">About Us</a><a href="#">Printing Services</a><a href="#">Operation Hours</a><a href="#">Mission Statement</a><a href="#">Locate Us</a><a href="#">Client Login</a>
    </div>

    <h3 style="left:625px">Social Links</h3>
    <div class="col" style="left:625px">
      <div class="social">
        <span style="background:#3b5b98">Friendsy</span>
        <span style="background:#3aa0d8">Chirper</span>
        <span style="background:#2a6fa8">Linkwork</span>
        <span style="background:#e98a22">Feedline</span>
      </div>
      <span class="like">Like <b>162</b></span>
    </div>

    <h3 style="left:787px">Feedback</h3>
    <div class="col feedback-col" style="left:787px;top:56px">
      <div class="fb-field">Name (required)</div>
      <div class="fb-field">Email (required)</div>
      <div class="fb-field msg">Message (required)</div>
      <div class="fb-submit">SUBMIT</div>
    </div>
  </footer>
  <div class="abs copyright">Copyright © 2013 HPW Online</div>

</div>
</body>
</html>
```